Personal Business Card

I am an award winning banjo player who plays with two different professional bands. My experiences include studio recordings for other artists and played the theme song for the Creature Channel's "Frontier Tundra Nights". I am ready to take my career to the next level and would like something that will look professional. it is important to me to have a banjo on the card. If possible my accomplishments to be put on back of card.

Industry/Entity Type

Artists

Contact Information for Business Card

Morgan Pell
cell 602-315-2860
email morganpellbanjo@quillpost.net

2008 AZ Banjo Champion
2008 Pinemeadow Banjo Champion
2010 AZ Banjo Champion
2010 Copper Creek Gathering Halvorn Banjo Champion
2010 Birchstone Hollow Fair Banjo Finalist

```html
<!DOCTYPE html>
<html lang="en">
<head>
<meta charset="utf-8">
<title>Morgan Pell – Business Card</title>
<link rel="stylesheet" href="https://fonts.googleapis.com/css2?family=Abril+Fatface&family=Jost:wght@400&display=swap">
<style>
  :root {
    --ink: #111111;
    --board: #000000;
    --paper: #ffffff;
    --page: #ffffff;
    --ghost: #e9e9e9;
  }
  html, body {
    margin: 0;
    padding: 0;
    width: 1200px;
    height: 800px;
    overflow: hidden;
    background: var(--page);
  }
  .board {
    position: absolute;
    left: 262px;
    top: 0;
    width: 720px;
    height: 800px;
    background: var(--board);
  }
  .card {
    position: absolute;
    width: 521px;
    height: 303px;
    background: var(--paper);
  }
  .card svg { display: block; width: 100%; height: 100%; }
  .card--front { left: 369px; top: 55px; }
  .card--back  { left: 374px; top: 438px; }
  .name-arc {
    font-family: "Abril Fatface", serif;
    font-size: 50px;
    fill: var(--ink);
  }
  .contact {
    font-family: "Jost", sans-serif;
    font-size: 13.5px;
    fill: var(--ink);
    text-anchor: middle;
  }
  .award {
    font-family: "Abril Fatface", serif;
    font-size: 17px;
    fill: var(--ink);
  }
</style>
</head>
<body>
  <div class="board"></div>

  <section class="card card--front" aria-label="Business card front">
    <svg viewBox="0 0 538 313">
      <defs>
        <path id="arc-first" d="M 128 192 A 220 220 0 0 1 244 148"/>
        <path id="arc-last" d="M 316 148 A 220 220 0 0 1 432 192"/>
        <linearGradient id="banjo-tone" x1="0" y1="0" x2="0" y2="1">
          <stop offset="0" stop-color="#2a2a2a"/>
          <stop offset="1" stop-color="#0d0d0d"/>
        </linearGradient>
      </defs>
      <text class="name-arc"><textPath href="#arc-first" textLength="120" lengthAdjust="spacingAndGlyphs">MORGAN</textPath></text>
      <text class="name-arc"><textPath href="#arc-last" textLength="120" lengthAdjust="spacingAndGlyphs">PELL</textPath></text>
      <rect class="banjo-art" role="img" aria-label="Banjo illustration, upright, black on white"
            x="253" y="30" width="54" height="212" rx="27" fill="url(#banjo-tone)"/>
      <text class="contact" x="279" y="268">602-315-2860</text>
      <text class="contact" x="279" y="284">email morganpellbanjo@quillpost.net</text>
    </svg>
  </section>

  <section class="card card--back" aria-label="Business card back">
    <svg viewBox="0 0 538 313">
      <defs>
        <radialGradient id="ghost-tone" cx="0.2" cy="0.85" r="0.9">
          <stop offset="0" stop-color="var(--ghost)"/>
          <stop offset="1" stop-color="#ffffff"/>
        </radialGradient>
      </defs>
      <rect class="ghost-banjo" role="img" aria-label="Faint banjo illustration lying diagonally"
            x="0" y="40" width="260" height="273" fill="url(#ghost-tone)"/>
      <g class="awards">
        <rect role="img" aria-label="Banjo headstock bullet" x="182" y="64" width="13" height="16" rx="3" fill="var(--ink)"/>
        <text class="award" x="206" y="78" textLength="155" lengthAdjust="spacingAndGlyphs">2008 AZ Banjo Champion</text>

        <rect role="img" aria-label="Banjo headstock bullet" x="153" y="108" width="13" height="16" rx="3" fill="var(--ink)"/>
        <text class="award" x="177" y="122" textLength="212" lengthAdjust="spacingAndGlyphs">2008 Pinemeadow Banjo Champion</text>

        <rect role="img" aria-label="Banjo headstock bullet" x="182" y="151" width="13" height="16" rx="3" fill="var(--ink)"/>
        <text class="award" x="206" y="165" textLength="155" lengthAdjust="spacingAndGlyphs">2010 AZ Banjo Champion</text>

        <rect role="img" aria-label="Banjo headstock bullet" x="105" y="195" width="13" height="16" rx="3" fill="var(--ink)"/>
        <text class="award" x="128" y="209" textLength="308" lengthAdjust="spacingAndGlyphs">2010 Copper Creek Gathering Halvorn Banjo Champion</text>

        <rect role="img" aria-label="Banjo headstock bullet" x="122" y="238" width="13" height="16" rx="3" fill="var(--ink)"/>
        <text class="award" x="146" y="252" textLength="272" lengthAdjust="spacingAndGlyphs">2010 Birchstone Hollow Fair Banjo Finalist</text>
      </g>
    </svg>
  </section>
</body>
</html>
```